Starting meadery needs logo and label design

We are starting to show our hand crafted meads to potential investors and need a professional logo and label to properly show how serious this proj...

Target Market(s)

Craft beer drinker searching for a new experience. People who are beer drinkers aspiring to be wine drinker.

Industry/Entity Type

It Professional

Requirements
Must have
• Professional design. Not overly ornate. Simple use of colors for low cost startup printing.

```html
<!DOCTYPE html>
<html lang="en">
<head>
<meta charset="utf-8">
<title>Orange Blossom Mead – Label Colourways</title>
<link rel="stylesheet" href="https://fonts.googleapis.com/css2?family=Josefin+Sans:wght@400;700&family=Sofia&display=swap">
<style>
  :root {
    --canvas: #ffffff;
    --ink: #111111;
    --brown: #8a5a2b;
    --label-ivory: #efe9ea;
    --label-rose: #ecbcbb;
    --label-butter: #efe9b8;
    --label-mist: #dde1e8;
  }
  * { box-sizing: border-box; margin: 0; padding: 0; }
  html, body {
    width: 1200px; height: 900px; overflow: hidden;
    background: var(--canvas);
  }
  .canvas {
    position: relative; width: 1200px; height: 900px;
    display: flex; justify-content: center; align-items: center; gap: 43px;
  }
  .label {
    width: 240px; height: 320px;
    display: flex; flex-direction: column; align-items: center;
    padding-top: 22px;
  }
  .label--ivory { background: var(--label-ivory); }
  .label--rose { background: var(--label-rose); }
  .label--butter { background: var(--label-butter); }
  .label--mist { background: var(--label-mist); }

  .brand {
    height: 170px;
    display: flex; flex-direction: column; align-items: center; justify-content: center;
    gap: 12px;
  }
  .brand__dot {
    width: 56px; height: 56px; border-radius: 50%;
    background: var(--brown);
  }
  .brand__name {
    font-family: "Josefin Sans", sans-serif;
    font-weight: 700;
    font-size: 21px;
    letter-spacing: 1px;
    line-height: 1.15;
    text-align: center;
    color: var(--brown);
    text-transform: uppercase;
  }
  .flavour {
    margin-top: 14px;
    font-family: "Josefin Sans", sans-serif;
    font-weight: 400;
    font-size: 15px;
    color: var(--ink);
  }
  .product {
    font-family: "Josefin Sans", sans-serif;
    font-weight: 700;
    font-size: 42px;
    line-height: 1;
    letter-spacing: 2px;
    color: var(--ink);
    text-shadow: 3px 2px 0 rgba(0,0,0,0.35);
    margin-top: 2px;
  }
  .description {
    margin-top: 12px;
    width: 214px;
    font-family: "Sofia", cursive;
    font-size: 8.2px;
    line-height: 13px;
    text-align: center;
    color: var(--ink);
  }
</style>
</head>
<body>
<main class="canvas">
  <section class="label label--ivory">
    <div class="brand"><span class="brand__dot"></span><p class="brand__name">Bramblecote<br>Meadery</p></div>
    <p class="flavour">Orange blossom</p>
    <h2 class="product">MEAD</h2>
    <p class="description">Lorem ipsum dolor sit amet, Lorem ipsum dolor sit amet, consectetuer adipiscing elit, sed diam nonummy nibh euismod tincidunt ut laoreet dolore magna aliquam erat volutpat. Ut wisi enim ad minim veniam, quis nostrud</p>
  </section>
  <section class="label label--rose">
    <div class="brand"><span class="brand__dot"></span><p class="brand__name">Bramblecote<br>Meadery</p></div>
    <p class="flavour">Orange blossom</p>
    <h2 class="product">MEAD</h2>
    <p class="description">Lorem ipsum dolor sit amet, Lorem ipsum dolor sit amet, consectetuer adipiscing elit, sed diam nonummy nibh euismod tincidunt ut laoreet dolore magna aliquam erat volutpat. Ut wisi enim ad minim veniam, quis nostrud</p>
  </section>
  <section class="label label--butter">
    <div class="brand"><span class="brand__dot"></span><p class="brand__name">Bramblecote<br>Meadery</p></div>
    <p class="flavour">Orange blossom</p>
    <h2 class="product">MEAD</h2>
    <p class="description">Lorem ipsum dolor sit amet, Lorem ipsum dolor sit amet, consectetuer adipiscing elit, sed diam nonummy nibh euismod tincidunt ut laoreet dolore magna aliquam erat volutpat. Ut wisi enim ad minim veniam, quis nostrud</p>
  </section>
  <section class="label label--mist">
    <div class="brand"><span class="brand__dot"></span><p class="brand__name">Bramblecote<br>Meadery</p></div>
    <p class="flavour">Orange blossom</p>
    <h2 class="product">MEAD</h2>
    <p class="description">Lorem ipsum dolor sit amet, Lorem ipsum dolor sit amet, consectetuer adipiscing elit, sed diam nonummy nibh euismod tincidunt ut laoreet dolore magna aliquam erat volutpat. Ut wisi enim ad minim veniam, quis nostrud</p>
  </section>
</main>
</body>
</html>
```